Web Page Design for a Website that Provides Tutoring

I am looking to create an online tutoring website. The website will allow parents or students to contact tutors with a view to instructing them to tutor themselves or their children.

The name of the website is LendYourLessons.

This brief is to create the design for one of the web pages for this web site. I am hoping the same designer will be available to design other pages.

The page I want designed is one of the more complex and I have attached the design as an excel spreadsheet. The web page needs to include all the items on this page but if you want to change the positioning of the items then Im fine with that.

I recently had two logos created for this website. My favourite is the one with a mortar board but im not sure I like the colours. I have attached both of these logos and you can use either of them, change the colours or create something different. I just want a design pleasing to the eye. If the logo is changed I would like that in a seperate file.

So can you please submit designs for this page. I have attached the two logos which you can use, change or if you feel you have a better idea then you can use that.

On the spreadsheet the Send Message, Favourite etc are buttons.

Target Market(s)

People who want to better themselves.
Possible middle class to upper class.

Industry/Entity Type

Tutoring

Number of Pages Required

1 page

Requirements
Must have
• The designs must have alot of the information attached in the spreadsheet.

```html
<!DOCTYPE html>
<html lang="en">
<head>
<meta charset="utf-8">
<title>LendYourLessons – Tutor Profile</title>
<link href="https://fonts.googleapis.com/css2?family=Roboto:wght@300;400;500;700&display=swap" rel="stylesheet">
<style>
:root{
  --ink:#222;
  --dark:#2b2b2b;
  --board:#2f2f2f;
  --blue:#3a5a98;
  --heading-blue:#2d4f8f;
  --orange:#f26b3a;
  --red:#f01414;
  --green:#3d6b1e;
  --cal-blue:#2f5597;
  --grey-band:#c6c6c6;
  --cell:#e9e9e9;
  --line:#bdbdbd;
  --white:#fff;
  --muted:#555;
  --star:#f05a24;
}
*{box-sizing:border-box;margin:0;padding:0}
html,body{width:1200px;height:3000px;overflow:hidden;background:var(--white)}
body{font-family:"Roboto",Arial,sans-serif;color:var(--ink);position:relative}
.abs{position:absolute}

/* top bar */
.topbar{left:0;top:0;width:1200px;height:40px;background:var(--dark)}
.search{left:644px;top:6px;width:310px;height:26px;background:var(--white);font-size:11px;color:#444;padding:7px 12px}
.search svg{position:absolute;right:10px;top:4px}
.account{left:970px;top:9px;color:var(--white);font-size:13px;display:flex;gap:14px;align-items:center}
.account span{display:flex;align-items:center;gap:6px}
.account i{display:inline-block;width:16px;height:16px;border:2px solid #e6b422;border-radius:50%}
.account b{display:inline-block;width:16px;height:16px;background:#e6b422;border-radius:2px}

/* header */
.header{left:0;top:40px;width:1200px;height:112px;background:var(--white);box-shadow:0 2px 4px rgba(0,0,0,.15);z-index:2}
.brand{left:100px;top:50px;display:flex;align-items:center;gap:10px;font-size:22px;font-weight:700;color:var(--heading-blue)}
.brand i{display:block;width:28px;height:28px;background:var(--orange)}
.nav{left:530px;top:0;height:112px;display:flex}
.nav-item{width:116px;height:112px;display:flex;flex-direction:column;align-items:center;justify-content:center;gap:10px;font-size:11px;letter-spacing:2px;font-weight:500;color:#444;border-right:2px dotted #777;position:relative}
.nav-item:last-child{border-right:none}
.nav-item svg{stroke:#444;fill:none;stroke-width:2}

/* hero */
.hero{left:0;top:152px;width:1200px;height:456px;background:radial-gradient(ellipse at 50% 40%,#4a4a4a,var(--board) 70%,#1e1e1e)}
.hero-photo{left:94px;top:198px;width:414px;height:370px;background:var(--white);padding:8px}
.hero-photo div{width:100%;height:100%;background:linear-gradient(135deg,#8ea8a2,#c9b49a 45%,#3c5d7a)}
.tutor-name{left:642px;top:208px;color:var(--white);font-size:15px;font-weight:500;letter-spacing:.5px}
.tutor-name small{display:block;font-size:10px;font-weight:500;margin-top:4px}
.bio{left:552px;top:260px;width:556px;height:228px;background:var(--white);padding:20px 24px 0 26px;font-size:11.5px;line-height:1.55;color:#444}
.bio p+p{margin-top:12px}
.bio em{color:var(--red);font-style:italic}
.btn{display:flex;align-items:center;justify-content:center;color:var(--white);font-size:12px;font-weight:500;letter-spacing:.3px}
.btn-send{left:640px;top:510px;width:146px;height:44px;background:var(--orange)}
.btn-fav{left:798px;top:510px;width:146px;height:44px;background:var(--blue)}
.btn-review{left:956px;top:510px;width:146px;height:44px;background:var(--blue)}

/* stats */
.stats-band{left:0;top:608px;width:1200px;height:170px;background:var(--grey-band)}
.stats{left:96px;top:644px;width:688px;border-collapse:collapse;background:var(--cell);font-size:13px}
.stats td{height:33px;border:1px solid var(--line);padding:0 12px}
.stats th{width:202px;background:var(--dark);color:var(--white);text-align:left;padding:0 12px;font-weight:700;border-bottom:1px solid #555}
.stats td.member{text-align:center;font-weight:500}
.feedback-box{left:784px;top:644px;width:326px;height:100px;background:var(--cell);border:1px solid var(--line)}
.btn-feedback{left:830px;top:676px;width:230px;height:34px;background:var(--blue)}

/* subjects */
.section-title{left:106px;top:796px;font-size:50px;font-weight:400;color:var(--heading-blue);letter-spacing:.5px}
.rates{left:96px;top:868px;width:736px;border-collapse:collapse;background:var(--cell);font-size:12.5px}
.rates td{height:33px;border:1px solid var(--line);padding:0 14px}
.rates thead td{height:34px}
.rates th{width:202px;background:var(--dark);color:var(--white);text-align:left;padding:0 12px;font-size:15px;font-weight:500}
.rates th span{display:flex;justify-content:space-between;align-items:center}
.rates th svg{stroke:#ddd;fill:none;stroke-width:1.5}
.side-photo{left:838px;top:868px;width:270px;height:504px;background:linear-gradient(160deg,#c98a6a,#e5d2b8 40%,#6b5a8a 80%,#3a2f4a)}
.legend{left:96px;top:976px;width:202px;font-size:11px;color:var(--white);font-weight:500}
.legend div{height:24px;padding:5px 12px;margin-bottom:1px}
.call{left:96px;top:1110px;font-size:12px;font-weight:500}
.call strong{display:block;font-size:25px;font-weight:500;margin:6px 0 2px}
.call small{font-size:11.5px}

/* calendar */
.calendar{left:302px;top:976px;width:530px;height:396px;border:1px solid var(--line)}
.cal-head{height:48px;display:flex;align-items:center;justify-content:space-between;padding:0 18px;font-size:14px;color:#444}
.cal-head b{font-size:32px;font-weight:400;color:#222}
.cal-days{display:grid;grid-template-columns:repeat(7,1fr);background:var(--dark);color:var(--white);font-size:12px;text-align:center;height:20px;line-height:20px}
.cal-grid{display:grid;grid-template-columns:repeat(7,1fr);grid-auto-rows:65.4px}
.cal-grid div{border-right:1px solid var(--line);border-bottom:1px solid var(--line);font-size:25px;padding:2px 6px;color:#111}
.cal-grid .t{background:var(--orange);color:var(--white)}
.cal-grid .n{background:var(--red);color:var(--white)}
.cal-grid .r{background:var(--cal-blue);color:var(--white)}
.cal-grid .a{background:var(--green);color:var(--white)}

/* banner */
.banner{left:0;top:1400px;width:1200px;height:422px;background:linear-gradient(90deg,#2a3a32,#3f5a48 55%,#2e4536)}
.banner-photo{left:0;top:1400px;width:470px;height:422px;background:linear-gradient(120deg,#6c7d72,#d8b59a 40%,#e8e2da 70%,#4a5a50)}
.banner-text{left:484px;top:1540px;color:var(--white)}
.banner-text h2{font-size:44px;font-weight:500}
.banner-text p{font-size:33px;font-weight:300}
.banner-text p.small{font-size:26px;margin-top:4px}

/* reviews */
.reviews-title{left:0;top:1846px;width:1200px;text-align:center;font-size:29px;font-weight:500}
.lead-photo{left:522px;top:1896px;width:156px;height:156px;border-radius:50%;background:linear-gradient(160deg,#5a7a6a,#a8a196 60%,#2f4a3e)}
.lead-name{left:0;top:2070px;width:1200px;text-align:center;font-size:14px;font-weight:500;color:var(--heading-blue)}
.lead-sub{left:0;top:2090px;width:1200px;text-align:center;font-size:12.5px;color:#333}
.stars{color:var(--star);letter-spacing:1px}
.stars .off{color:#999}
.lead-stars{left:0;top:2112px;width:1200px;text-align:center;font-size:22px}
.review{width:400px}
.review-avatar{width:80px;height:80px;border-radius:50%;background:linear-gradient(150deg,#b07a5e,#e0c0a8 60%,#6a4a3a)}
.review-meta{font-size:12px;color:var(--heading-blue);display:flex;gap:8px;align-items:center;font-weight:500}
.review-meta svg{stroke:#333;fill:none;stroke-width:1.6}
.review-body{font-size:12px;line-height:1.55;color:#444;margin-top:12px;text-align:justify}
.review-author{margin-top:14px;font-size:14px;font-weight:500;color:var(--heading-blue)}
.review-role{font-size:12px;color:#333}
.review-stars{font-size:20px;margin-top:2px}

/* form */
.form-photo{left:96px;top:2480px;width:464px;height:334px;background:linear-gradient(120deg,#d7c4a4,#9a6a4e 40%,#e8e0d4 70%,#7a8a6a)}
.form-title{left:592px;top:2502px;font-size:29px;font-weight:500}
.form-rating{left:594px;top:2552px;font-size:14px;color:#444;display:flex;gap:8px;align-items:center}
.form-rating span{font-size:20px;color:#888;letter-spacing:1px}
.field{border:1px solid #ccc;font-size:11px;color:#777;padding:9px 10px;background:var(--white)}
.f-name{left:594px;top:2588px;width:446px;height:34px}
.f-teacher{left:594px;top:2628px;width:218px;height:34px}
.f-subject{left:820px;top:2628px;width:220px;height:34px}
.f-comments{left:594px;top:2668px;width:446px;height:80px}
.btn-submit{left:594px;top:2758px;width:446px;height:34px;background:var(--blue)}

/* footer */
.footer{left:0;top:2860px;width:1200px;height:140px;background:var(--dark);color:var(--white);text-align:center}
.footer-links{margin-top:34px;font-size:12px}
.footer-links span{margin:0 14px}
.copyright{margin-top:8px;font-size:12px}
.social{margin-top:14px;display:flex;justify-content:center;gap:6px}
.social i{display:block;width:28px;height:28px;border-radius:50%;background:#6a6a6a}
</style>
</head>
<body>

<div class="abs topbar"></div>
<div class="abs search">Search by keywords
  <svg width="18" height="18" viewBox="0 0 18 18"><circle cx="7" cy="7" r="5" fill="none" stroke="#222" stroke-width="2"/><line x1="11" y1="11" x2="16" y2="16" stroke="#222" stroke-width="2.4"/></svg>
</div>
<div class="abs account"><span><i></i>Login</span><span><b></b>Register</span></div>

<header class="abs header">
  <div class="abs brand" style="top:12px"><i></i>LendYourLessons</div>
  <nav class="abs nav">
    <div class="nav-item"><svg width="30" height="28" viewBox="0 0 30 28"><path d="M3 14 15 3l12 11M7 11v15h16V11"/></svg>HOME</div>
    <div class="nav-item"><svg width="30" height="30" viewBox="0 0 30 30"><circle cx="15" cy="15" r="12"/><line x1="15" y1="13" x2="15" y2="22"/><circle cx="15" cy="9" r="1"/></svg>ABOUT US</div>
    <div class="nav-item"><svg width="34" height="28" viewBox="0 0 34 28"><path d="M2 10 17 4l15 6-15 6zM8 13v8c5 4 13 4 18 0v-8"/></svg>STUDENT</div>
    <div class="nav-item"><svg width="34" height="30" viewBox="0 0 34 30"><circle cx="17" cy="7" r="4"/><path d="M9 26v-6c0-4 16-4 16 0v6M3 28h28"/></svg>TUTOR</div>
    <div class="nav-item"><svg width="30" height="30" viewBox="0 0 30 30"><path d="M5 12c0-6 20-6 20 0l-4 2-2-3h-8l-2 3zM8 16h14l3 10H5z"/></svg>CONTACT US</div>
  </nav>
</header>

<section class="abs hero"></section>
<div class="abs hero-photo"><div role="img" aria-label="Photo of a tutor helping a student with a textbook in front of a chalkboard"></div></div>
<div class="abs tutor-name">GARETH LINWOOD<small>( WOKING - TUTOR)</small></div>
<div class="abs bio">
  <p><em>Hi my name is Gareth !</em> I am a Contrary to popular belief, Lorem Ipsum is not simply random text. It has roots in a piece of classical Latin literature from 45 BC, making it over 2000 years old. Edwin Marlowe, a Latin professor at Eastbrook College in Virginia, looked up one of the more obscure Latin words, consectetur, from a Lorem Ipsum passage, and going through the cites of the word in classical literature, discovered the undoubtable source. Lorem Ipsum comes from sections</p>
  <p>Contrary to popular belief, Lorem Ipsum is not simply random text. It has roots in a piece of classical Latin literature from 45 BC, making it over 2000 years old. Edwin Marlowe, a Latin professor at Eastbrook College in Virginia, looked</p>
</div>
<div class="abs btn btn-send">SEND MESSAGE</div>
<div class="abs btn btn-fav">FAVOUR TUTOR</div>
<div class="abs btn btn-review">WRITE REVIEW</div>

<section class="abs stats-band"></section>
<table class="abs stats">
  <tr><th>Review Score</th><td>4.5 / 5</td><td class="member">Member Since 2014</td></tr>
  <tr><th>Reliability</th><td>4.0 / 5.0</td><td class="member">Last Logged In 16/12/2016</td></tr>
  <tr><th>Punctuality</th><td>4.6/5</td><td></td></tr>
</table>
<div class="abs feedback-box"></div>
<div class="abs btn btn-feedback">LEAVE FEEDBACK</div>

<h1 class="abs section-title">Subjects Taught</h1>
<table class="abs rates">
  <thead><tr><td style="width:202px">Subjects</td><td>Primary</td><td>Secondary GCSE</td><td>A-LEVEL</td><td>University Adult Learner</td></tr></thead>
  <tr><th><span>Biology<svg width="26" height="20" viewBox="0 0 26 20"><circle cx="13" cy="10" r="6"/><path d="M2 10h5M19 10h5M13 1v3M13 16v3"/></svg></span></th><td>£20</td><td>£20</td><td>£20</td><td>£50</td></tr>
  <tr><th><span>Chemistry<svg width="28" height="18" viewBox="0 0 28 18"><circle cx="8" cy="9" r="5"/><circle cx="20" cy="9" r="5"/><path d="M13 9h2"/></svg></span></th><td>£20</td><td>£20</td><td>£20</td><td>£50</td></tr>
</table>
<div class="abs side-photo" role="img" aria-label="Photo of a smiling tutor holding folders"></div>

<div class="abs legend">
  <div style="background:var(--green)">AVAILABLE</div>
  <div style="background:var(--orange)">TAKEN</div>
  <div style="background:var(--cal-blue)">RESERVED</div>
  <div style="background:var(--red)">NO</div>
</div>
<div class="abs call">
  <svg width="40" height="40" viewBox="0 0 40 40"><path d="M8 4l7 7-4 5c2 5 6 9 11 11l5-4 7 7-5 6C16 36 4 24 2 9z" fill="#111"/><path d="M24 6a10 10 0 0 1 10 10M24 12a4 4 0 0 1 4 4" stroke="#111" stroke-width="2" fill="none"/></svg><br>
  Call us at<strong>123 - 555 -0147</strong><small>and Reserved Tutor</small>
</div>

<div class="abs calendar">
  <div class="cal-head"><span>PRE</span><b>2016 DECEMBER</b><span>NEXT</span></div>
  <div class="cal-days"><span>SUN</span><span>MON</span><span>TUE</span><span>WED</span><span>THU</span><span>FRI</span><span>SAT</span></div>
  <div class="cal-grid">
    <div></div><div></div><div></div><div></div><div class="t">1</div><div>2</div><div>3</div>
    <div>4</div><div class="t">5</div><div>6</div><div class="t">7</div><div>8</div><div>9</div><div class="t">10</div>
    <div class="n">11</div><div>12</div><div>13</div><div>14</div><div class="t">15</div><div>16</div><div class="r">17</div>
    <div class="r">18</div><div class="a">19</div><div class="r">20</div><div>21</div><div class="a">22</div><div>23</div><div class="a">24</div>
    <div class="n">25</div><div>26</div><div class="a">27</div><div>28</div><div>29</div><div>30</div><div>31</div>
  </div>
</div>

<section class="abs banner"></section>
<div class="abs banner-photo" role="img" aria-label="Photo of a smiling teacher holding chalk at a green board"></div>
<div class="abs banner-text">
  <h2>Contrary to popular belief</h2>
  <p>Lorem Ipsum is not simply random text.</p>
  <p class="small">classical Latin literature from 45 BC,</p>
</div>

<h2 class="abs reviews-title">Tutor's Reviews</h2>
<div class="abs lead-photo" role="img" aria-label="Portrait of the tutor at a chalkboard"></div>
<div class="abs lead-name">Mr. Owen Ridley (Chemistry Proffesor)</div>
<div class="abs lead-sub">has 2 Reviews with an average of 4.0</div>
<div class="abs lead-stars stars">★★★★</div>

<div class="abs review-avatar" style="left:154px;top:2174px" role="img" aria-label="Student portrait"></div>
<article class="abs review" style="left:252px;top:2174px;width:374px">
  <div class="review-meta">
    <svg width="16" height="16" viewBox="0 0 16 16"><rect x="2" y="3" width="12" height="11"/><line x1="2" y1="7" x2="14" y2="7"/></svg>Date: 12/12/2016
    <svg width="16" height="16" viewBox="0 0 16 16"><circle cx="8" cy="8" r="6"/><path d="M8 4v4h3"/></svg>Time: 10;30 am
  </div>
  <p class="review-body">Contrary to popular belief, Lorem Ipsum is not simply random text. It has roots in a piece of classical Latin literature from 45 BC, making it over 2000 years old. Edwin Marlowe, a Latin professor at Eastbrook College in Virginia, looked up one of the more obscure Latin words, consectetur,</p>
  <div class="review-author">Student name will come here</div>
  <div class="review-role">(Chemistry Student)</div>
  <div class="review-stars stars">★★★★<span class="off">★</span></div>
</article>

<div class="abs review-avatar" style="left:620px;top:2174px" role="img" aria-label="Student portrait"></div>
<article class="abs review" style="left:714px;top:2174px;width:322px">
  <div class="review-meta">
    <svg width="16" height="16" viewBox="0 0 16 16"><rect x="2" y="3" width="12" height="11"/><line x1="2" y1="7" x2="14" y2="7"/></svg>Date: 12/12/2016
    <svg width="16" height="16" viewBox="0 0 16 16"><circle cx="8" cy="8" r="6"/><path d="M8 4v4h3"/></svg>Time: 10;30 am
  </div>
  <p class="review-body">Contrary to popular belief, Lorem Ipsum is not simply random text. It has roots in a piece of classical Latin literature from 45 BC, making it over 2000 years old. Edwin Marlowe, a Latin professor at Eastbrook College in Virginia, looked up one of the more obscure Latin words, consectetur,</p>
  <div class="review-author">Student name will come here</div>
  <div class="review-role">(Chemistry Student)</div>
  <div class="review-stars stars">★★★★<span class="off">★</span></div>
</article>

<div class="abs form-photo" role="img" aria-label="Photo of a teacher helping students at their desks in a classroom"></div>
<h2 class="abs form-title">Student Review Form</h2>
<div class="abs form-rating">Review :<span>☆☆☆☆☆</span></div>
<div class="abs field f-name">Enter your name</div>
<div class="abs field f-teacher">Select teacher's name</div>
<div class="abs field f-subject">Select subject</div>
<div class="abs field f-comments">Comments (maximum 350 words)</div>
<div class="abs btn btn-submit">SUBMIT YOUR FEEDBACK</div>

<footer class="abs footer">
  <div class="footer-links"><span>Home</span>|<span>About Us</span>|<span>Student</span>|<span>Tutor</span>|<span>Contact Us</span></div>
  <div class="copyright">Copyright 2016, lendyourlessons.example. All Rights Reserved.</div>
  <div class="social"><i></i><i></i><i></i><i></i></div>
</footer>

</body>
</html>
```